Velmora Biz Card 2019

New business card for Velmora Property Inspections. We are a residential home inspection company in Arizona.

Target Market(s)

Real Estate

Font styles to use
Sans Serif

Requirements
Must have
• Glen Mirewick
• Home Inspector
• Velmora Property Inspections, LLC
• 480-555-0172
• glen@velmora-llc.example

```html
<!DOCTYPE html>
<html lang="en">
<head>
<meta charset="utf-8">
<title>Velmora Property Inspections – Business Card</title>
<link rel="stylesheet" href="https://fonts.googleapis.com/css2?family=Roboto:wght@400;500;700&display=swap">
<style>
  :root {
    --card-green: #167d00;
    --accent-lime: #4cff1f;
    --text-white: #ffffff;
  }
  html, body {
    margin: 0;
    padding: 0;
    width: 1200px;
    height: 687px;
    overflow: hidden;
    background: var(--card-green);
  }
  .business-card {
    position: relative;
    width: 1200px;
    height: 687px;
    background: var(--card-green);
    font-family: "Roboto", Arial, sans-serif;
    color: var(--text-white);
    overflow: hidden;
  }
  .company-name {
    position: absolute;
    left: 88px;
    top: 76px;
    margin: 0;
    font-size: 52px;
    font-weight: 400;
    line-height: 1;
    white-space: nowrap;
  }
  .brand-mark {
    position: absolute;
    left: 40px;
    top: 180px;
    display: flex;
    align-items: center;
    gap: 28px;
  }
  .brand-square {
    width: 150px;
    height: 150px;
    background: var(--accent-lime);
    flex: none;
  }
  .brand-name {
    margin: 0;
    font-size: 112px;
    font-weight: 500;
    line-height: 1;
    color: var(--accent-lime);
    white-space: nowrap;
  }
  .brand-mark { flex-direction: column; align-items: flex-start; gap: 22px; }
  .person {
    position: absolute;
    right: 193px;
    top: 220px;
    text-align: right;
  }
  .person-name {
    margin: 0;
    font-size: 72px;
    font-weight: 700;
    line-height: 1;
    white-space: nowrap;
  }
  .person-title {
    margin: 22px 0 0;
    font-size: 52px;
    font-weight: 500;
    line-height: 1;
    white-space: nowrap;
  }
  .contact {
    position: absolute;
    right: 70px;
    top: 498px;
    text-align: right;
    font-size: 52px;
    font-weight: 400;
    line-height: 61px;
    white-space: nowrap;
  }
  .contact p { margin: 0; }
</style>
</head>
<body>
  <main class="business-card">
    <h1 class="company-name">Velmora Property Inspections, LLC</h1>
    <div class="brand-mark">
      <span class="brand-square" aria-hidden="true"></span>
      <p class="brand-name">Velmora</p>
    </div>
    <section class="person">
      <h2 class="person-name">Glen Mirewick</h2>
      <p class="person-title">Home Inspector</p>
    </section>
    <section class="contact">
      <p class="contact-phone">480-555-0172</p>
      <p class="contact-email">glen@velmora-llc.example</p>
    </section>
  </main>
</body>
</html>
```